Realty Group Needs Classy, Contemporary Letterhead Design

We need a letterhead design for a new realty company located in NY, USA. We buy investment properties to rehabilitate and or keep in our rental portfolio.

```html
<!DOCTYPE html>
<html lang="en">
<head>
<meta charset="utf-8">
<title>Brightwater Realty Group Letterhead</title>
<link rel="stylesheet" href="https://fonts.googleapis.com/css2?family=Arimo:wght@400;700&display=swap">
<style>
  :root {
    --backdrop: #2e2f30;
    --brand-purple: #55279a;
    --brand-purple-deep: #47208b;
    --ink-purple: #4a2a8a;
    --paper: #ffffff;
    --paper-tint: #f7f6fb;
    --on-brand: #ffffff;
  }
  * { box-sizing: border-box; margin: 0; padding: 0; }
  html, body {
    width: 1200px; height: 800px; overflow: hidden;
    background: var(--backdrop);
    font-family: "Arimo", Arial, sans-serif;
  }
  .canvas {
    position: relative; width: 1200px; height: 800px;
    display: flex; justify-content: center; align-items: center;
  }
  .letterhead {
    position: relative; width: 540px; height: 764px;
    background: var(--paper-tint);
    color: var(--ink-purple);
    display: flex; flex-direction: column;
  }
  .masthead {
    position: relative; height: 121px;
    background: linear-gradient(180deg, var(--brand-purple) 0%, var(--brand-purple-deep) 100%);
    color: var(--on-brand);
  }
  .masthead-rule {
    position: absolute; top: 6px; left: 0; right: 0;
    height: 2px; background: var(--on-brand); opacity: .9;
  }
  .sender-details {
    position: absolute; left: 24px; top: 20px;
    list-style: none; font-size: 10px; line-height: 16.4px;
  }
  .sender-details .company { font-weight: 700; font-size: 11px; }
  .brand-name {
    position: absolute; left: 150px; width: 240px; top: 40px;
    text-align: center; font-weight: 700; font-size: 13px;
    letter-spacing: .5px; line-height: 20px; color: var(--on-brand);
  }
  .brand-name .primary { font-size: 30px; line-height: 34px; letter-spacing: 0; display: block; }
  .recipient-block {
    position: absolute; left: 430px; top: 42px;
    font-size: 10px; line-height: 16.4px; font-style: normal;
  }
  .date-strip {
    height: 42px; background: var(--paper);
    border-bottom: 2px solid var(--brand-purple-deep);
    display: flex; align-items: center; justify-content: center;
    font-size: 15.5px; color: var(--ink-purple);
  }
  .letter-body {
    flex: 1; padding: 90px 64px 0 75px;
    font-size: 11px; line-height: 20.2px;
  }
  .salutation { margin-bottom: 20px; }
  .letter-body p { margin: 0; }
  .closing { margin-top: 20px; }
  .signature { margin-top: 20px; }
  .footer-band {
    height: 8px; background: var(--brand-purple-deep);
  }
</style>
</head>
<body>
<main class="canvas">
  <article class="letterhead">
    <header class="masthead">
      <div class="masthead-rule"></div>
      <ul class="sender-details">
        <li class="company">Business Company</li>
        <li>Business person</li>
        <li>0555-214-630 :P</li>
        <li>318400 P.O. Box</li>
        <li>10472 NY US</li>
        <li>brightwaterny.com</li>
      </ul>
      <div class="brand-name">
        <span class="primary">BRIGHTWATER</span>
        Realty Group, LLC
      </div>
      <address class="recipient-block">
        First Last Name<br>
        Street Address<br>
        00000 City, State
      </address>
    </header>
    <div class="date-strip">December, 28.2021</div>
    <section class="letter-body">
      <p class="salutation">Dear; Person Name</p>
      <p>Lorem ipsum dolor sit amet, consectetur adipiscing elit. Aenean ut ipsum eget massa hendrerit vestibulum vel in velit. Donec pretium neque velit.</p>
      <p>Aliquam porta lectus nec mauris ornare venenatis. Vivamus non est turpis, et cursus sem. Mauris vehicula erat in diam auctor at bibendum nisl lacinia.</p>
      <p>Morbi imperdiet neque vehicula nunc convallis gravida. Vestibulum iaculis pretium placerat. Integer consequat, est sit amet facilisis eleifend, nibh nibh varius orci, eget dapibus arcu dui non purus. Pellentesque in magna mauris. Duis enim sapien, dictum vitae condimentum a, pulvinar vel lacus. Mauris et molestie nibh. Vestibulum vitae nulla at metus elementum porta sit amet interdum elit. Nulla sollicitudin neque eu nulla volutpat congue.</p>
      <p>Etiam pellentesque, velit id dapibus fermentum, turpis sapien ornare dui, ac tincidunt ligula odio congue purus. Nunc sed ante dui, in porta lectus. Cras nec sem lorem. In hac habitasse platea dictumst. Maecenas id diam quis dui porta tristique. Sed id egestas felis. Donec ullamcorper mattis posuere. Phasellus fermentum eleifend tortor vel dapibus. Vestibulum ante ipsum.</p>
      <p class="closing">Sincerely,</p>
      <p class="signature">Sender Name</p>
    </section>
    <footer class="footer-band"></footer>
  </article>
</main>
</body>
</html>
```